Letterhead design for Sleep Consulting Business

I'm looking for a new letterhead (heading/footer) design for my Sleep Consulting Business, I work with families to help their children improve their sleep.

The heading/footer will used in Microsoft Word Only-to be used for all of my documents such as writing Sleep Plans. I need to utilize as much working space in the document as possible. This will NOT be printed out on paper- it will only be used for heading/footer on microsoft word, then emailed to clients, who may print it at home.

My brand colors:
Dark Blue Hex: 1F2A42
Lighter Blueish Hex: 90BEC9
You're welcome to check out my website for inspiration- it is freshly created with other colors as well, and I love the outcome. www.hollowpinerest.com

Target Market(s)

Tired parents

Font styles to use
Script
Other font styles liked:
• Great Vibe, Lato or Just Another Hand are all used currently for my brand. Open to other options.

Requirements
Must have
• The letterhead (heading/footer) MUST be kept narrow (height-wise), so I have plenty of space on my document, while including important information.

It should look professional on screen, and when printed.

Must include my business name OR logo (Hollow Pine Sleep Consulting), and my email address. Mara@hollowpinerest.com

Website is optional, not required, just if you need to fill in a spot: www.hollowpinerest.com

```html
<!DOCTYPE html>
<html lang="en">
<head>
<meta charset="utf-8">
<title>Hollow Pine Sleep Consulting — Letterhead</title>
<link href="https://fonts.googleapis.com/css2?family=Lato:wght@400;700&family=Kaushan+Script&display=swap" rel="stylesheet">
<style>
  :root {
    --navy: #1f2a42;
    --sky: #90bec9;
    --ink: #555a60;
    --paper: #ffffff;
    --backdrop: #c9cacc;
  }
  * { margin: 0; padding: 0; box-sizing: border-box; }
  html, body { width: 1200px; height: 909px; overflow: hidden; }
  body {
    background: var(--backdrop);
    font-family: "Lato", sans-serif;
    position: relative;
  }
  .letterhead {
    position: absolute;
    left: 267px; top: 24px;
    width: 666px; height: 861px;
    background: var(--paper);
    box-shadow: 0 4px 18px rgba(0,0,0,0.18);
    overflow: hidden;
    color: var(--ink);
  }
  .brand {
    position: absolute; left: 52px; top: 46px;
    display: flex; align-items: center; gap: 10px;
  }
  .brand-dot {
    width: 34px; height: 34px; border-radius: 50%;
    background: var(--navy);
  }
  .brand-name {
    font-size: 20px; font-weight: 400; color: var(--navy);
    letter-spacing: 0.3px;
  }
  .letter {
    position: absolute; left: 78px; top: 150px; width: 530px;
    font-size: 11.5px; line-height: 16.5px;
  }
  .letter-date { margin-bottom: 14px; }
  .recipient { margin-left: 18px; }
  .recipient-block { margin-bottom: 14px; }
  .company { margin-left: 36px; margin-bottom: 16px; }
  .salutation {
    margin-left: 54px; font-weight: 700; font-size: 15px;
    margin-bottom: 18px; color: #4a4f55;
  }
  .body-text { margin-left: 72px; }
  .body-text p { margin-bottom: 16px; }
  .closing { margin-left: 108px; margin-top: 26px; }
  .signature {
    margin-left: 150px; margin-top: 6px;
    font-family: "Kaushan Script", cursive;
    font-size: 34px; color: #4a4f55;
  }
  .footer-band {
    position: absolute; left: 0; bottom: 0; width: 666px; height: 110px;
  }
  .footer-email {
    position: absolute; right: 26px; bottom: 18px;
    display: flex; align-items: center; gap: 6px;
    color: var(--paper); font-size: 11.5px;
  }
</style>
</head>
<body>
  <main class="letterhead">
    <header class="brand">
      <span class="brand-dot"></span>
      <span class="brand-name">Hollow Pine Sleep Consulting</span>
    </header>

    <section class="letter">
      <p class="letter-date">June -22-2020</p>
      <div class="recipient recipient-block">
        <p>Mr, Owen Hale</p>
        <p>President</p>
      </div>
      <div class="company">
        <p>Brightfield Group</p>
        <p>48 Orchard Lane, Suite# 7</p>
        <p>Fairview, State, 204517</p>
      </div>
      <p class="salutation">Dear Mr, Owen</p>
      <div class="body-text">
        <p>Lorem ipsum dolor sit amet, consectetur adipisicing elit, sed do eiusmod tempor incididunt ut labore et dolore magna aliqua. Ut enim ad minim veniam, quis nostrud exercitation ullamco laboris nisi ut aliquip ex ea commodo consequat. Duis aute irure dolor in reprehenderit in voluptate velit esse cillum dolore eu fugiat nulla pariatur.</p>
        <p>Lorem ipsum dolor sit amet, consectetur adipisicing elit, sed do eiusmod tempor incididunt ut labore et dolore magna aliqua. Ut enim ad minim veniam, quis nostrud exercitation ullamco laboris nisi ut aliquip ex ea commodo consequat. Duis aute irure dolor in reprehenderit in voluptate velit esse cillum dolore eu fugiat nulla pariatur.</p>
        <p>Lorem ipsum dolor sit amet, consectetur adipisicing elit, sed do eiusmod tempor incididunt ut labore et dolore magna aliqua. Ut enim ad minim veniam, quis nostrud exercitation ullamco laboris nisi ut aliquip ex ea commodo consequat.</p>
        <p>Excepteur sint occaecat cupidatat non proident, sunt in culpa qui officia deserunt mollit anim id est laborum. re et dolore magnam aliquam quaerat voluptatem.</p>
      </div>
      <p class="closing">Regards</p>
      <p class="signature">Daniel Reyes</p>
    </section>

    <svg class="footer-band" viewBox="0 0 666 110" preserveAspectRatio="none" aria-hidden="true">
      <path d="M0 96 C230 92 430 60 666 8" fill="none" stroke="var(--sky)" stroke-width="5"/>
      <path d="M0 110 L0 104 C240 100 440 70 666 20 L666 110 Z" fill="var(--navy)"/>
    </svg>
    <div class="footer-email">
      <svg width="12" height="9" viewBox="0 0 12 9" aria-hidden="true">
        <rect x="0.5" y="0.5" width="11" height="8" fill="none" stroke="var(--sky)"/>
        <path d="M0.5 0.5 L6 5 L11.5 0.5" fill="none" stroke="var(--sky)"/>
      </svg>
      <span>Mara@hollowpinerest.com</span>
    </div>
  </main>
</body>
</html>
```